Stationery Design for a fast food resturaunt

We just created our logo, we need nice stationary to go with it. We beed the design to be on white background and black background.

Target Market(s)

Landlords who will lease their retail shops to us. Shopping Mall Management.Real Estate Professionals.

Font styles to use
Sans Serif

```html
<!DOCTYPE html>
<html lang="en">
<head>
<meta charset="utf-8">
<title>Amber Hive Stationery</title>
<link rel="stylesheet" href="https://fonts.googleapis.com/css2?family=Arimo:wght@400;700&display=swap">
<style>
  :root{
    --canvas:#e4e4e4;
    --paper:#f4f4f4;
    --paper-edge:#ececec;
    --ink:#222222;
    --dark:#1f1f1f;
    --darker:#0c0c0c;
    --amber:#f7a900;
    --white:#ffffff;
    --rule:#d6d6d6;
    --muted:#555555;
  }
  *{margin:0;padding:0;box-sizing:border-box}
  html,body{width:1200px;height:900px;overflow:hidden}
  body{background:var(--canvas);font-family:"Arimo",Arial,sans-serif;color:var(--ink);position:relative}
  .item{position:absolute}
  .brand{font-family:"Arimo",Arial,sans-serif;font-weight:400;color:var(--amber);letter-spacing:1px;line-height:1;display:flex;align-items:center;gap:6px;white-space:nowrap}
  .brand-mark{display:inline-block;background:var(--amber)}

  /* letterhead */
  .letterhead{left:206px;top:60px;width:372px;height:525px;background:var(--paper)}
  .letterhead .brand{position:absolute;left:33px;top:30px;font-size:19px}
  .letterhead .brand-mark{width:12px;height:12px}
  .divider{position:absolute;width:1px;background:var(--rule)}
  .letterhead .divider{left:222px;top:20px;height:62px}
  .contact{position:absolute;font-size:7px;color:var(--ink);line-height:11.5px}
  .contact .address{font-size:8.5px;margin-bottom:3px}
  .contact-row{display:flex;align-items:center;gap:3px}
  .contact-icon{width:8px;height:8px;background:var(--amber);border-radius:1.5px;display:inline-block}
  .letterhead .contact{left:251px;top:28px}
  .foot-bar{position:absolute;left:0;bottom:0;height:6px;background:var(--amber)}
  .foot-tab{position:absolute;right:0;bottom:0;background:var(--darker);color:var(--white);display:flex;align-items:center;justify-content:flex-end;clip-path:polygon(8px 0,100% 0,100% 100%,0 100%)}
  .letterhead .foot-bar{width:222px}
  .letterhead .foot-tab{width:147px;height:13px;font-size:8.5px;padding-right:24px}

  /* folder */
  .folder{left:640px;top:47px;width:448px;height:538px}
  .folder-cover{position:absolute;left:0;top:0;width:428px;height:538px;background:var(--dark)}
  .folder-spine{position:absolute;top:0;width:2px;height:538px;background:#111}
  .folder-tab{position:absolute;left:428px;top:363px;width:20px;height:175px;background:var(--darker);clip-path:polygon(0 0,100% 18px,100% 100%,0 100%)}
  .folder .brand{position:absolute;left:292px;top:452px;font-size:18px}
  .folder .brand-mark{width:11px;height:11px}

  /* pencil */
  .pencil{left:119px;top:280px;width:16px;height:295px}
  .pencil-label{position:absolute;left:3px;top:236px;width:10px;font-size:5px;color:var(--amber);writing-mode:vertical-rl;letter-spacing:.5px}

  /* business cards */
  .card-front{left:73px;top:627px;width:171px;height:97px;background:var(--dark);display:flex;align-items:center;justify-content:center}
  .card-front .brand{font-size:14px}
  .card-front .brand-mark{width:9px;height:9px}
  .card-back{left:72px;top:749px;width:170px;height:97px;background:var(--paper)}
  .person{position:absolute;left:23px;top:37px;font-size:6px;line-height:8px}
  .person strong{font-size:6.5px;font-weight:700;display:block}
  .card-back .divider{left:74px;top:21px;height:46px}
  .card-back .contact{left:96px;top:30px;font-size:5px;line-height:9px}
  .card-back .contact-icon{width:6px;height:6px}
  .card-back .foot-bar{width:100px;height:3px}
  .card-back .foot-tab{width:70px;height:8px;font-size:5px;padding-right:9px}

  /* envelope */
  .envelope-front{left:286px;top:639px;width:413px;height:203px;background:var(--paper)}
  .envelope-front .brand{position:absolute;left:32px;top:30px;font-size:17px}
  .envelope-front .brand-mark{width:11px;height:11px}
  .envelope-front .foot-bar{width:282px;height:4px}
  .envelope-front .foot-tab{width:131px;height:13px;font-size:9px;padding-right:20px}
  .envelope-back{left:735px;top:640px;width:413px;height:202px;background:var(--paper)}
</style>
</head>
<body>

<section class="item letterhead" aria-label="Letterhead">
  <div class="brand"><span class="brand-mark"></span>AMBER HIVE</div>
  <div class="divider"></div>
  <div class="contact">
    <div class="address">Address Street 88</div>
    <div class="contact-row"><span class="contact-icon"></span>+01.2345.6789</div>
    <div class="contact-row"><span class="contact-icon"></span>+0123.4567</div>
    <div class="contact-row"><span class="contact-icon"></span>contact@email.com</div>
  </div>
  <div class="foot-bar"></div>
  <div class="foot-tab">www.amberhive.com</div>
</section>

<section class="item folder" aria-label="Presentation folder">
  <div class="folder-cover"></div>
  <div class="folder-spine" style="left:8px"></div>
  <div class="folder-spine" style="left:16px"></div>
  <div class="folder-tab"></div>
  <div class="brand"><span class="brand-mark"></span>AMBER HIVE</div>
</section>

<section class="item pencil" aria-label="Branded pencil">
  <svg width="16" height="295" viewBox="0 0 16 295">
    <polygon points="8,0 2,22 14,22" fill="#d9c3a0"/>
    <polygon points="8,0 6.5,7 9.5,7" fill="#333"/>
    <rect x="2" y="22" width="12" height="270" fill="#2a2a2a"/>
    <rect x="2" y="288" width="12" height="7" rx="3" fill="#2a2a2a"/>
  </svg>
  <div class="pencil-label">AMBER HIVE</div>
</section>

<section class="item card-front" aria-label="Business card front">
  <div class="brand"><span class="brand-mark"></span>AMBER HIVE</div>
</section>

<section class="item card-back" aria-label="Business card back">
  <div class="person"><strong>Full Name</strong>Occupation</div>
  <div class="divider"></div>
  <div class="contact">
    <div class="contact-row"><span class="contact-icon"></span>+01.2345.6789</div>
    <div class="contact-row"><span class="contact-icon"></span>+0123.4567</div>
    <div class="contact-row"><span class="contact-icon"></span>contact@email.com</div>
  </div>
  <div class="foot-bar"></div>
  <div class="foot-tab">www.amberhive.com</div>
</section>

<section class="item envelope-front" aria-label="Envelope front">
  <div class="brand"><span class="brand-mark"></span>AMBER HIVE</div>
  <div class="foot-bar"></div>
  <div class="foot-tab">www.amberhive.com</div>
</section>

<section class="item envelope-back" aria-label="Envelope back">
  <svg width="413" height="202" viewBox="0 0 413 202">
    <polyline points="2,2 16,70 397,70 411,2" fill="none" stroke="#cfcfcf" stroke-width="1"/>
  </svg>
</section>

</body>
</html>
```